GPS Fleet Management web application design

We need an application UI design for a GPS fleet management application.
This is a WEB APPLICATION that will run in a desktop browser and not a mobile app design. Looking for a UI/UX expert with experience building desktop application designs.
UI needs to display map with real time location of fleet vehicles
Elements of the application would include things like reporting, geofencing, vehicle on-map displays, alerts, vehicle tabular listing with status (Online, offline, etc), vehicle detail info display like speed, engine rpm, etc etc.
You can blorvex vehicle tracking and get a sense of different GUIs. It is CRITICAL for the designer to understand fleet management applications to be able to do justice to the experience that we are trying to build and be successful in this project.
Looking for something different from the ordinary layout and with some GUI innovation. Should be simple to use, pleasant to look at with proper use of colors and very intuitive. We need a proper framework and user experience built and then on top of that we can add more panes and functionality as needed.
Some UX ideas include hiding things that are not required and resurfacing them easily on demand, being able to move panes around like a canvas, a comprehensive dashboard style layout on login and proper visualization of real time elements as they change.
Once we get some samples we will help the designer perfect it but we need to get some professional UI/UX person to conceptualize and design the user experience.
Reason: Added more time to be able to provide feedback
Gps

```html
<!DOCTYPE html>
<html lang="en">
<head>
<meta charset="utf-8">
<title>GPS Fleet Management – Web Application</title>
<link href="https://fonts.googleapis.com/css2?family=Roboto:wght@300;400;500;700;900&display=swap" rel="stylesheet">
<style>
:root{
  --ink-dark:#1d1f24;
  --brand-blue:#0d4fd6;
  --header-blue:#2176e6;
  --brand-panel:#1c69d8;
  --accent:#1a6fe0;
  --text:#1f2329;
  --muted:#6b7280;
  --line:#e3e7ee;
  --sidebar:#f0f3f8;
  --idle-bar:#d9dbe0;
  --white:#ffffff;
}
*{box-sizing:border-box;margin:0;padding:0}
html,body{width:1200px;height:1200px;overflow:hidden;background:var(--ink-dark);font-family:'Roboto',sans-serif;color:var(--text)}
.stage{position:absolute;left:0;top:0;width:1500px;height:1500px;transform:scale(.8);transform-origin:0 0}
.backdrop{position:absolute;inset:0}
.abs{position:absolute}
.board-title{left:110px;top:88px;font-size:48px;font-weight:700;color:var(--white);letter-spacing:-.5px}
.board-sub{left:110px;top:153px;font-size:37px;font-weight:300;color:var(--white)}
.board-tag{right:112px;top:1333px;font-size:36px;font-weight:300;color:var(--white)}
.app{left:110px;top:250px;width:1280px;height:1000px;background:var(--white);border-radius:6px;overflow:hidden}
.topbar{left:0;top:0;width:1280px;height:60px;background:var(--header-blue)}
.brand{left:0;top:0;width:250px;height:60px;background:var(--brand-panel);display:flex;align-items:center;padding-left:22px;gap:14px;color:var(--white);font-size:19px;font-weight:500}
.brand-mark{width:30px;height:30px;border-radius:50%;background:var(--white);opacity:.95}
.search{left:893px;top:15px;width:187px;height:30px;border-radius:15px;background:#1b63c9;color:#a9c6f2;font-size:15px;padding:6px 14px}
.avatar{left:1151px;top:13px;width:34px;height:34px;border-radius:50%;background:linear-gradient(135deg,#cfd6e0,#6d7784)}
.logout{left:1203px;top:21px;color:var(--white);font-size:13px;font-weight:500}
.sidebar{left:0;top:60px;width:250px;height:940px;background:var(--sidebar)}
.menu-label{left:20px;top:22px;font-size:15px;letter-spacing:3px;color:var(--muted)}
.nav-item{left:0;width:250px;height:54px;display:flex;align-items:center;padding-left:20px;gap:14px;font-size:20px;color:var(--text)}
.nav-item svg{width:20px;height:20px}
.nav-item.is-active{background:var(--white);color:var(--accent);font-weight:500}
.badge{left:203px;top:363px;width:24px;height:24px;border-radius:50%;background:var(--accent);color:var(--white);font-size:15px;text-align:center;line-height:24px}
.page-title{left:275px;top:95px;font-size:36px;font-weight:900;letter-spacing:.5px}
.section-title{left:275px;top:156px;font-size:18px;font-weight:500}
.section-date{left:275px;top:182px;font-size:13px;color:var(--accent);letter-spacing:.3px}
.select{border:1px solid #d4d8df;border-radius:3px;display:flex;align-items:center;justify-content:space-between;padding:0 12px;font-size:17px;color:var(--text)}
.perf-select{left:711px;top:158px;width:284px;height:35px}
.tab{top:158px;height:35px;font-size:17px;line-height:35px}
.tab.is-on{left:1020px;width:68px;background:var(--accent);color:var(--white);text-align:center;border-radius:3px}
.card{background:var(--white);border:1px solid var(--line);border-radius:3px;box-shadow:0 1px 4px rgba(0,0,0,.06)}
.kpi-card{left:275px;top:228px;width:480px;height:259px}
.kpi-divider{left:239px;top:15px;width:1px;height:228px;background:var(--line)}
.kpi{position:absolute;text-align:center;width:200px;color:var(--accent)}
.kpi-big{font-size:46px;font-weight:700}
.kpi-label{color:var(--text);font-size:17px;margin-top:8px}
.kpi-sub{position:absolute;text-align:center;width:120px;color:var(--accent)}
.kpi-sub b{display:block;font-size:28px;font-weight:300}
.kpi-sub span{font-size:15px}
.chart-card{left:775px;top:228px;width:480px;height:259px}
.map-card{left:275px;top:508px;width:980px;height:399px}
.map-area{left:14px;top:13px;width:466px;height:370px;background:linear-gradient(150deg,#e6e8ec 0%,#dfe4ea 45%,#c9dcf2 70%,#e2e4e8 100%)}
.pin{position:absolute;width:36px;height:36px;border-radius:50%;background:var(--accent);border:2px solid var(--white);color:var(--white);font-size:16px;font-weight:500;text-align:center;line-height:32px}
.map-title{left:498px;top:22px;font-size:26px;font-weight:300}
.veh-select{left:500px;top:65px;width:173px;height:35px}
.id-search{left:684px;top:65px;width:242px;height:35px;color:#9aa1ab}
.table{left:500px;top:115px;width:460px}
.row{position:relative;height:40px;display:flex;align-items:center;font-size:15.5px;border-bottom:1px solid var(--line)}
.row.head{font-weight:500;border-bottom:none;height:36px}
.row.is-sel{background:#f7f8fa}
.radio{position:absolute;left:7px;width:15px;height:15px;border-radius:50%;border:1px solid #c5cad2;background:var(--white)}
.radio.on::after{content:"";position:absolute;left:3px;top:3px;width:7px;height:7px;border-radius:50%;background:var(--accent)}
.c-id{position:absolute;left:33px}
.c-status{position:absolute;left:105px;display:flex;align-items:center;gap:8px}
.c-loc{position:absolute;left:288px}
.c-pin{position:absolute;left:426px;top:9px}
.hl{color:var(--accent)}
.caret{display:inline-block;border-left:5px solid transparent;border-right:5px solid transparent;border-top:5px solid var(--text);margin-left:5px;vertical-align:middle}
.scroll{left:955px;top:152px;width:4px;height:105px;border-radius:2px;background:#c9ced6}
.footer{left:0;top:945px;width:1280px;padding-left:250px;text-align:center;font-size:14px;letter-spacing:1.3px;color:#555}
</style>
</head>
<body>
<div class="stage">
  <svg class="backdrop" width="1500" height="1500" viewBox="0 0 1500 1500"><rect width="1500" height="1500" fill="#1d1f24"/><polygon points="1500,0 1500,1500 0,1500" fill="#0d4fd6"/></svg>

  <div class="abs board-title">GPS Fleet Management</div>
  <div class="abs board-sub">Web Application</div>
  <div class="abs board-tag">UI Design Concept</div>

  <div class="abs app">
    <div class="abs topbar"></div>
    <div class="abs brand"><span class="brand-mark"></span>Fleet Management</div>
    <div class="abs search">Search
      <svg style="position:absolute;right:12px;top:8px" width="14" height="14" viewBox="0 0 14 14"><circle cx="6" cy="6" r="4.5" fill="none" stroke="#fff" stroke-width="2"/><line x1="9.5" y1="9.5" x2="13" y2="13" stroke="#fff" stroke-width="2"/></svg>
    </div>
    <svg class="abs" style="left:1104px;top:18px" width="26" height="26" viewBox="0 0 26 26"><path d="M6 19h14l-2-3v-5a5 5 0 0 0-10 0v5z" fill="none" stroke="#fff" stroke-width="2" stroke-linejoin="round"/><circle cx="13" cy="21.5" r="1.8" fill="#fff"/><circle cx="20" cy="5" r="5" fill="#1d1f24"/><text x="20" y="8.3" font-size="9" fill="#fff" text-anchor="middle" font-family="Roboto,sans-serif">2</text></svg>
    <div class="abs avatar" role="img" aria-label="User profile photo"></div>
    <div class="abs logout">⇥ Logout</div>

    <div class="abs sidebar">
      <div class="abs menu-label">MENU</div>
      <div class="abs nav-item is-active" style="top:57px"><svg viewBox="0 0 20 20" fill="#1a6fe0"><rect x="1" y="2" width="8" height="7" rx="1"/><rect x="11" y="2" width="8" height="7" rx="1"/><rect x="1" y="11" width="8" height="7" rx="1"/><rect x="11" y="11" width="8" height="7" rx="1"/></svg>Overview</div>
      <div class="abs nav-item" style="top:115px"><svg viewBox="0 0 20 20"><circle cx="10" cy="10" r="8" fill="#2a2d33"/><path d="M6 7l4 1 1 4-3 2z" fill="#f0f3f8"/></svg>Map</div>
      <div class="abs nav-item" style="top:173px"><svg viewBox="0 0 20 20" fill="#2a2d33"><rect x="2" y="5" width="10" height="9" rx="1"/><path d="M12 8h4l2 3v3h-6z"/><circle cx="6" cy="15.5" r="2"/><circle cx="15" cy="15.5" r="2"/></svg>Vehicle</div>
      <div class="abs nav-item" style="top:231px"><svg viewBox="0 0 20 20"><circle cx="10" cy="10" r="8" fill="#2a2d33"/><circle cx="6" cy="9" r="1.5" fill="#f0f3f8"/><circle cx="10" cy="6" r="1.5" fill="#f0f3f8"/><circle cx="14" cy="9" r="1.5" fill="#f0f3f8"/><circle cx="10" cy="13" r="2" fill="#f0f3f8"/></svg>Drivers</div>
      <div class="abs nav-item" style="top:289px"><svg viewBox="0 0 20 20"><rect x="1" y="5" width="18" height="12" rx="2" fill="#2a2d33"/><rect x="6" y="3" width="8" height="3" fill="#2a2d33"/><circle cx="10" cy="11" r="3.5" fill="#f0f3f8"/></svg>Cameras</div>
      <div class="abs nav-item" style="top:347px"><svg viewBox="0 0 20 20"><path d="M4 1h8l5 5v13H4z" fill="#2a2d33"/></svg>Reports</div>
      <div class="abs badge">2</div>
      <div class="abs nav-item" style="top:405px"><svg viewBox="0 0 20 20"><circle cx="10" cy="10" r="6.5" fill="none" stroke="#2a2d33" stroke-width="4" stroke-dasharray="3 2"/><circle cx="10" cy="10" r="5" fill="#2a2d33"/><circle cx="10" cy="10" r="2" fill="#f0f3f8"/></svg>Settings</div>
    </div>

    <div class="abs page-title">OVERVIEW</div>
    <div class="abs section-title">Fleet Performance</div>
    <div class="abs section-date">20 Sep, 2017&nbsp; 1:23PM</div>
    <div class="abs select perf-select">Vehicle Usage &amp; Performance <svg width="12" height="8" viewBox="0 0 12 8"><path d="M1 1l5 5 5-5" fill="none" stroke="#1a6fe0" stroke-width="2"/></svg></div>
    <div class="abs tab is-on">Daily</div>
    <div class="abs tab" style="left:1108px">Weekly</div>
    <div class="abs tab" style="left:1186px">Monthly</div>

    <div class="abs card kpi-card">
      <div class="abs kpi-divider"></div>
      <div class="kpi" style="left:20px;top:44px"><div class="kpi-big">80%</div><div class="kpi-label">ACTIVE VEHICLES</div></div>
      <div class="kpi" style="left:258px;top:44px"><div class="kpi-big">1.52</div><div class="kpi-label">FUEL USAGE ( L / KM )</div></div>
      <div class="kpi-sub" style="left:7px;top:163px"><b>20</b><span>Active</span></div>
      <div class="kpi-sub" style="left:104px;top:163px"><b>25</b><span>All</span></div>
      <div class="kpi-sub" style="left:247px;top:163px"><b>1.48</b><span>Yesterday</span></div>
      <div class="kpi-sub" style="left:358px;top:163px"><b><small style="font-size:13px">▲</small> 2.7 <small style="font-size:15px">%</small></b><span>Saving</span></div>
    </div>

    <div class="abs card chart-card">
      <svg width="480" height="259" viewBox="886 478 480 259" font-family="Roboto,sans-serif">
        <text x="901" y="511" font-size="18" font-weight="500" fill="#1f2329">Total Usage</text>
        <text x="1175" y="511" font-size="17" fill="#1a6fe0">Work Hours</text>
        <text x="1282" y="511" font-size="17" fill="#6b7280">Distance</text>
        <g font-size="13" fill="#333" text-anchor="end">
          <text x="922" y="542">8K</text><text x="922" y="572">6K</text><text x="922" y="602">4K</text><text x="922" y="632">2K</text><text x="922" y="662">0</text>
        </g>
        <g stroke="#e6e8ec"><line x1="930" y1="537" x2="1348" y2="537"/><line x1="930" y1="567" x2="1348" y2="567"/><line x1="930" y1="597" x2="1348" y2="597"/><line x1="930" y1="627" x2="1348" y2="627"/><line x1="930" y1="657" x2="1348" y2="657"/></g>
        <g fill="#1a6fe0">
          <rect x="942" y="576" width="10" height="81"/><rect x="979" y="606" width="10" height="51"/><rect x="1016" y="560" width="10" height="97"/><rect x="1053" y="609" width="10" height="48"/><rect x="1090" y="555" width="10" height="102"/><rect x="1127" y="575" width="10" height="82"/><rect x="1164" y="560" width="10" height="97"/><rect x="1201" y="583" width="10" height="74"/><rect x="1238" y="560" width="10" height="97"/><rect x="1275" y="583" width="10" height="74"/><rect x="1312" y="574" width="10" height="83"/>
        </g>
        <g fill="#d9dbe0">
          <rect x="954" y="620" width="10" height="37"/><rect x="991" y="590" width="10" height="67"/><rect x="1028" y="636" width="10" height="21"/><rect x="1065" y="587" width="10" height="70"/><rect x="1102" y="641" width="10" height="16"/><rect x="1139" y="621" width="10" height="36"/><rect x="1176" y="636" width="10" height="21"/><rect x="1213" y="613" width="10" height="44"/><rect x="1250" y="636" width="10" height="21"/><rect x="1287" y="613" width="10" height="44"/><rect x="1324" y="623" width="10" height="34"/>
        </g>
        <g font-size="11" fill="#1a6fe0" text-anchor="end">
          <text transform="translate(957 672) rotate(-40)">10 SEP</text><text transform="translate(994 672) rotate(-40)">11 SEP</text><text transform="translate(1031 672) rotate(-40)">12 SEP</text><text transform="translate(1068 672) rotate(-40)">13 SEP</text><text transform="translate(1105 672) rotate(-40)">14 SEP</text><text transform="translate(1142 672) rotate(-40)">15 SEP</text><text transform="translate(1179 672) rotate(-40)">16 SEP</text><text transform="translate(1216 672) rotate(-40)">17 SEP</text><text transform="translate(1253 672) rotate(-40)">18 SEP</text><text transform="translate(1290 672) rotate(-40)">19 SEP</text><text transform="translate(1327 672) rotate(-40)">20 SEP</text>
        </g>
        <circle cx="1076" cy="714" r="3.5" fill="#1a6fe0"/><text x="1085" y="719" font-size="13" fill="#333">Active</text>
        <circle cx="1147" cy="714" r="3.5" fill="#c9ccd2"/><text x="1156" y="719" font-size="13" fill="#333">Idle</text>
      </svg>
    </div>

    <div class="abs card map-card">
      <div class="abs map-area" role="img" aria-label="City street map with river and live vehicle positions">
        <div class="pin" style="left:274px;top:29px">002</div>
        <div class="pin" style="left:157px;top:220px">001</div>
      </div>
      <div class="abs map-title">Map View</div>
      <div class="abs select veh-select">All Vehicles <svg width="12" height="8" viewBox="0 0 12 8"><path d="M1 1l5 5 5-5" fill="none" stroke="#1a6fe0" stroke-width="2"/></svg></div>
      <div class="abs select id-search">Type ID or Model <svg width="18" height="18" viewBox="0 0 18 18"><circle cx="7.5" cy="7.5" r="5.5" fill="none" stroke="#1f2329" stroke-width="2.2"/><line x1="11.5" y1="11.5" x2="16" y2="16" stroke="#1f2329" stroke-width="2.2"/></svg></div>
      <svg class="abs" style="left:940px;top:73px" width="20" height="18" viewBox="0 0 20 18" stroke="#1f2329" stroke-width="1.8"><line x1="1" y1="3" x2="19" y2="3"/><line x1="1" y1="9" x2="19" y2="9"/><line x1="1" y1="15" x2="19" y2="15"/><rect x="11" y="1" width="3" height="4" fill="#fff"/><rect x="5" y="7" width="3" height="4" fill="#fff"/><rect x="12" y="13" width="3" height="4" fill="#fff"/></svg>

      <div class="abs table">
        <div class="row head"><span class="radio"></span><span class="c-id">ID<i class="caret"></i></span><span class="c-status">Status<i class="caret"></i></span><span class="c-loc">Location<i class="caret"></i></span></div>
        <div class="row"><span class="radio"></span><span class="c-id">001</span><span class="c-status"><svg width="20" height="14" viewBox="0 0 20 14" fill="#1a6fe0"><rect x="6" y="1" width="13" height="9" rx="1"/><path d="M1 5h4v5H1z"/><circle cx="5" cy="11.5" r="2"/><circle cx="15" cy="11.5" r="2"/></svg>Active <span class="hl">(64km/h)</span></span><span class="c-loc">Springfield, TN</span><svg class="c-pin" width="16" height="22" viewBox="0 0 16 22"><path d="M8 1a7 7 0 0 0-7 7c0 5 7 13 7 13s7-8 7-13a7 7 0 0 0-7-7z" fill="#1a6fe0"/><circle cx="8" cy="8" r="3" fill="#fff"/></svg></div>
        <div class="row is-sel"><span class="radio on"></span><span class="c-id">002</span><span class="c-status"><svg width="20" height="14" viewBox="0 0 20 14" fill="#1a6fe0"><rect x="6" y="1" width="13" height="9" rx="1"/><path d="M1 5h4v5H1z"/><circle cx="5" cy="11.5" r="2"/><circle cx="15" cy="11.5" r="2"/></svg>Active <span class="hl">(68km/h)</span></span><span class="c-loc">Nashville, TN</span><svg class="c-pin" width="16" height="22" viewBox="0 0 16 22"><path d="M8 1a7 7 0 0 0-7 7c0 5 7 13 7 13s7-8 7-13a7 7 0 0 0-7-7z" fill="#1a6fe0"/><circle cx="8" cy="8" r="3" fill="#fff"/></svg></div>
        <div class="row is-sel"><span class="radio on"></span><span class="c-id">003</span><span class="c-status"><svg width="20" height="14" viewBox="0 0 20 14" fill="#1a6fe0"><rect x="6" y="1" width="13" height="9" rx="1"/><path d="M1 5h4v5H1z"/><circle cx="5" cy="11.5" r="2"/><circle cx="15" cy="11.5" r="2"/></svg>Active <span class="hl">(57km/h)</span></span><span class="c-loc">Nashville, TN</span><svg class="c-pin" width="16" height="22" viewBox="0 0 16 22"><path d="M8 1a7 7 0 0 0-7 7c0 5 7 13 7 13s7-8 7-13a7 7 0 0 0-7-7z" fill="#1a6fe0"/><circle cx="8" cy="8" r="3" fill="#fff"/></svg></div>
        <div class="row"><span class="radio"></span><span class="c-id">004</span><span class="c-status"><svg width="20" height="14" viewBox="0 0 20 14" fill="#a3a8b0"><rect x="6" y="1" width="13" height="9" rx="1"/><path d="M1 5h4v5H1z"/><circle cx="5" cy="11.5" r="2"/><circle cx="15" cy="11.5" r="2"/></svg>Idle <span class="hl">(2h)</span></span><span class="c-loc">Nashville, TN</span><svg class="c-pin" width="16" height="22" viewBox="0 0 16 22"><path d="M8 1a7 7 0 0 0-7 7c0 5 7 13 7 13s7-8 7-13a7 7 0 0 0-7-7z" fill="#1a6fe0"/><circle cx="8" cy="8" r="3" fill="#fff"/></svg></div>
        <div class="row"><span class="radio"></span><span class="c-id">005</span><span class="c-status"><svg width="20" height="14" viewBox="0 0 20 14" fill="#a3a8b0"><rect x="6" y="1" width="13" height="9" rx="1"/><path d="M1 5h4v5H1z"/><circle cx="5" cy="11.5" r="2"/><circle cx="15" cy="11.5" r="2"/></svg>Idle <span class="hl">(15min)</span></span><span class="c-loc">Los Angeles, LA</span><svg class="c-pin" width="16" height="22" viewBox="0 0 16 22"><path d="M8 1a7 7 0 0 0-7 7c0 5 7 13 7 13s7-8 7-13a7 7 0 0 0-7-7z" fill="#1a6fe0"/><circle cx="8" cy="8" r="3" fill="#fff"/></svg></div>
        <div class="row" style="border-bottom:none"><span class="radio"></span><span class="c-id">006</span><span class="c-status"><svg width="20" height="14" viewBox="0 0 20 14" fill="#a3a8b0"><rect x="6" y="1" width="13" height="9" rx="1"/><path d="M1 5h4v5H1z"/><circle cx="5" cy="11.5" r="2"/><circle cx="15" cy="11.5" r="2"/></svg>Stopped <span class="hl">(1-day)</span></span><span class="c-loc">Springfield, TN</span><svg class="c-pin" width="16" height="22" viewBox="0 0 16 22"><path d="M8 1a7 7 0 0 0-7 7c0 5 7 13 7 13s7-8 7-13a7 7 0 0 0-7-7z" fill="#1a6fe0"/><circle cx="8" cy="8" r="3" fill="#fff"/></svg></div>
      </div>
      <div class="abs scroll"></div>
    </div>

    <div class="abs footer">©&nbsp; Fleet Management 2017. All rights reserved.</div>
  </div>
</div>
</body>
</html>
```